Serenelle Aura Candle Box Package Design

Two box sizes:
14oz Candle in a box Gift Boxes - 4 x 4 x 6
4oz Candle in a box Gift Boxes - 3 x 3 x 3
Website: www.serenelleaura.com
IG: @serenelle.aura
My brand is a sophisticated brand with luxury candles made of coconut wax.  Serenelle Aura means bright life. Our candles represent hope and light.
You matter, you are worthy, powerful and beautiful!
Each candle is hand poured, vegan, environmentally conscious, uniquely scented and rooted in the importance of self care and community. We donate a percentage of our proceeds to organizations that seek to empower and enrich women.
At Serenelle Aura, we believe that positive energy can move mountains.
We strive to elevate that energy in every way possible. Our candles are handmade with confident positivity in mind - 100% vegan friendly, non-toxic and carefully crafted for optimal performance yet minimal impact on the environment.

```html
<!DOCTYPE html>
<html lang="en">
<head>
<meta charset="utf-8">
<title>Serenelle Aura – Coconut Wax Candle Box Dieline</title>
<link rel="stylesheet" href="https://fonts.googleapis.com/css2?family=Cormorant+Garamond:wght@500&family=Poiret+One&family=Questrial&family=Great+Vibes&display=swap">
<style>
  :root {
    --backdrop: #a5b2ab;
    --board: #eceeeb;
    --board-light: #f7f8f6;
    --board-shade: #e3e6e2;
    --rule: #1f1f1f;
    --ink: #2a2a28;
    --ink-soft: #4a4a46;
    --leaf: #a9b8b6;
  }
  * { box-sizing: border-box; margin: 0; padding: 0; }
  html, body { width: 1200px; height: 2310px; overflow: hidden; background: var(--backdrop); }
  .canvas { position: relative; width: 1200px; height: 2310px; }

  .dieline {
    position: absolute; left: 0; top: 672px;
    width: 1338px; height: 1090px;
    transform: scale(0.8969); transform-origin: 0 0;
  }
  .dieline__margin-vertical {
    position: absolute; left: 366px; top: 10px; width: 341px; height: 1072px;
    background: var(--board); border-radius: 40px;
  }
  .dieline__margin-horizontal {
    position: absolute; left: 0; top: 375px; width: 1334px; height: 342px;
    background: var(--board);
  }
  .dieline__cuts { position: absolute; inset: 0; }

  .face {
    position: absolute; width: 313px; height: 312px;
    background: linear-gradient(180deg, var(--board-light) 0%, #ffffff 45%, var(--board-shade) 100%);
    font-family: "Questrial", sans-serif; color: var(--ink);
  }
  .face--top { left: 381px; top: 77px; height: 312px; }
  .face--bottom { left: 381px; top: 703px; height: 312px; }
  .flap { position: absolute; left: 381px; width: 312px; background: var(--board-light); }
  .flap--top { top: 26px; height: 50px; border-radius: 22px 22px 0 0; }
  .flap--bottom { top: 1017px; height: 49px; border-radius: 0 0 22px 22px; background: var(--board-shade); }
  .glue-flap { position: absolute; left: 15px; top: 391px; width: 51px; height: 311px; background: var(--board); }

  .lid-mark {
    position: absolute; left: 0; right: 0; top: 140px; text-align: center;
    font-family: "Poiret One", sans-serif; font-size: 22px; letter-spacing: 2px; color: var(--ink);
  }
  .face--top .lid-mark { transform: rotate(180deg); }

  .brand { position: absolute; left: 0; right: 0; top: 22px; text-align: center; }
  .brand__name {
    font-family: "Poiret One", sans-serif; font-size: 30px; letter-spacing: 1px;
    color: var(--ink); line-height: 1;
  }
  .brand__line {
    margin-top: 10px; font-size: 9.5px; letter-spacing: 3.4px; color: var(--ink-soft);
  }
  .brand__line::before, .brand__line::after {
    content: ""; display: inline-block; width: 18px; height: 1px; background: var(--ink-soft);
    vertical-align: middle; margin: 0 6px;
  }
  .brand__script {
    margin-top: 4px; font-family: "Great Vibes", cursive; font-size: 11px; color: var(--ink-soft);
  }

  .benefits { position: absolute; left: 40px; top: 106px; list-style: none; }
  .benefits li {
    display: flex; align-items: center; height: 23.4px;
    font-size: 8.6px; color: var(--ink);
  }
  .benefits__icon {
    width: 9px; height: 9px; border: 1px solid var(--ink-soft); border-radius: 50%;
    margin-right: 7px; flex: none;
  }
  .benefits__icon--filled { background: var(--ink-soft); }

  .web {
    position: absolute; left: 0; right: 0; top: 268px; text-align: center;
    font-size: 12.5px; letter-spacing: 3px; color: var(--ink);
  }

  .about { position: absolute; left: 20px; right: 20px; top: 120px; font-size: 8.4px; line-height: 17.5px; color: var(--ink); }
  .about p + p { margin-top: 17.5px; }

  .scent {
    position: absolute; left: 17px; top: 148px; transform: rotate(-90deg); transform-origin: 0 0;
    font-size: 16px; letter-spacing: 1.5px; color: var(--ink-soft);
  }
  .product-title {
    position: absolute; left: 42px; top: 30px;
    font-family: "Cormorant Garamond", serif; font-weight: 500; font-size: 62px; line-height: 54px;
    color: var(--ink);
  }
  .leaf {
    position: absolute; left: 163px; top: 20px; width: 140px; height: 134px;
    background: radial-gradient(ellipse at 55% 45%, var(--leaf) 0%, rgba(169,184,182,0.55) 55%, rgba(169,184,182,0) 75%);
  }
  .features {
    position: absolute; left: 0; right: 0; top: 190px; text-align: center;
    font-size: 10.2px; color: var(--ink); white-space: nowrap;
  }
  .features span + span::before {
    content: ""; display: inline-block; width: 1px; height: 15px; background: var(--ink);
    vertical-align: middle; margin: 0 9px;
  }
  .net-weight {
    position: absolute; left: 0; right: 0; top: 268px; text-align: center;
    font-size: 13px; letter-spacing: 2.5px; color: var(--ink);
  }
</style>
</head>
<body>
<main class="canvas">
  <section class="dieline" aria-label="Candle box dieline">
    <div class="dieline__margin-vertical"></div>
    <div class="dieline__margin-horizontal"></div>

    <div class="flap flap--top"></div>
    <div class="flap flap--bottom"></div>
    <div class="glue-flap"></div>

    <div class="face face--top"><div class="lid-mark">Serenelle Aura</div></div>
    <div class="face face--bottom"><div class="lid-mark">Serenelle Aura</div></div>

    <!-- side panel: benefits -->
    <div class="face" style="left:67px; top:391px;">
      <div class="brand">
        <div class="brand__name">SERENELLE AURA</div>
        <div class="brand__line">HANDMADE CANDLES</div>
        <div class="brand__script">with purpose and love</div>
      </div>
      <ul class="benefits">
        <li><span class="benefits__icon"></span>Burn Time up to 30hrs</li>
        <li><span class="benefits__icon"></span>100% vegan friendly, non-toxic</li>
        <li><span class="benefits__icon"></span>Skin Safe</li>
        <li><span class="benefits__icon"></span>Slow Clean-burning</li>
        <li><span class="benefits__icon benefits__icon--filled"></span>Pet Friendly</li>
        <li><span class="benefits__icon"></span>Non-Toxic &nbsp;|&nbsp; Phthalate-Free &nbsp;|&nbsp; Paraben-Free</li>
      </ul>
      <div class="web">WWW.SERENELLEAURA.COM</div>
    </div>

    <!-- front panel -->
    <div class="face" style="left:381px; top:391px;">
      <div class="scent">COCONUT</div>
      <h1 class="product-title">Wax<br>Candle</h1>
      <div class="leaf" role="img" aria-label="Palm leaf illustration"></div>
      <div class="features"><span>100% vegan friendly</span><span>Non-Toxic</span><span>Slow Clean-burning</span></div>
      <div class="net-weight">4OZ. (113G)</div>
    </div>

    <!-- side panel: about -->
    <div class="face" style="left:694px; top:391px;">
      <div class="brand">
        <div class="brand__name">SERENELLE AURA</div>
        <div class="brand__line">HANDMADE CANDLES</div>
        <div class="brand__script">with purpose and love</div>
      </div>
      <div class="about">
        <p>Each candle is hand poured, vegan, environmentally conscious, uniquely scented and rooted in the importance of self care and community.</p>
        <p>We donate a percentage of our proceeds to organizations that seek to empower and enrich women.</p>
      </div>
      <div class="web">WWW.SERENELLEAURA.COM</div>
    </div>

    <!-- back panel -->
    <div class="face" style="left:1007px; top:391px;">
      <div class="scent">COCONUT</div>
      <div class="product-title" aria-hidden="true">Wax<br>Candle</div>
      <div class="leaf" role="img" aria-label="Palm leaf illustration"></div>
      <div class="features"><span>100% vegan friendly</span><span>Non-Toxic</span><span>Slow Clean-burning</span></div>
      <div class="web">WWW.SERENELLEAURA.COM</div>
    </div>

    <svg class="dieline__cuts" width="1338" height="1090" viewBox="0 0 1338 1090" fill="none" stroke="#1f1f1f" stroke-width="1.5">
      <path d="M380 390 V50 Q380 25 405 25 H668 Q693 25 693 50 V390"/>
      <path d="M380 702 V1042 Q380 1067 405 1067 H668 Q693 1067 693 1042 V702"/>
      <line x1="380" y1="76" x2="693" y2="76"/>
      <line x1="380" y1="1016" x2="693" y2="1016"/>
      <rect x="14" y="390" width="1306" height="312"/>
      <line x1="66" y1="390" x2="66" y2="702"/>
      <line x1="380" y1="390" x2="380" y2="702"/>
      <line x1="693" y1="390" x2="693" y2="702"/>
      <line x1="1006" y1="390" x2="1006" y2="702"/>
    </svg>
  </section>
</main>
</body>
</html>
```